Business card design needed

Our company background is that we provides transfers to and from the airport, social & corporate events, weddings.
We are also available for charter for birthday party, wine tastings, concerts, anniversary, school balls etc.
Our business cards have to reflect that we have a professional company, they are our first contact and have to stand out from the other 'players' in the market.

Industry/Entity Type

School

Contact Information for Business Card

VESTAR PTH, Teodor & Marguerite, mob: 0427 381 592, PO Box 284, Larkvale WA 6172, ABN 52 614 203 178, Lic 7169/2058,

Requirements
Must have
• Telephone number: 0427 381 592
Website: www.VESTARPTH.com.au
postal address: PO Box 284, Larkvale WA 6172
Licences: Lic 7169/2058

***If using the new photo (one with the bus and buildings behind it), if possible can the buildings be cropped out. Thanks
Nice to have
• would be nice to have the pics of the vehicle(s), preferred the Vel on the card but not too fussed.
Should not have
• Picture of vehicle we don't have in our fleet. (We ONLY have the Velarions and Murako Densa mini bus)

```html
<!DOCTYPE html>
<html lang="en">
<head>
<meta charset="utf-8">
<title>VESTAR PTH — Business Card</title>
<link rel="stylesheet" href="https://fonts.googleapis.com/css2?family=Fondamento&family=Crimson+Text&display=swap">
<style>
  :root {
    --navy: #0c1d42;
    --title-blue: #1855a0;
    --title-text: #eaf5ff;
    --ink: #0e2348;
    --left-top: #c8eef6;
    --left-mid: #e2f5f9;
    --left-bottom: #aee2ee;
    --right-light: #a9d6f1;
    --right-mid: #7dbde8;
    --right-deep: #5aaae0;
    --divider: #8fb3c8;
  }
  * { margin: 0; padding: 0; box-sizing: border-box; }
  html, body { width: 1200px; height: 691px; overflow: hidden; background: #ffffff; }
  .card {
    position: relative;
    width: 1200px;
    height: 691px;
    overflow: hidden;
    font-family: "Crimson Text", Georgia, serif;
  }
  .band {
    position: absolute;
    left: 0;
    width: 100%;
    background: var(--navy);
  }
  .band--top { top: 0; height: 28px; }
  .band--bottom { bottom: 0; height: 30px; }
  .panel {
    position: absolute;
    top: 28px;
    bottom: 30px;
  }
  .panel--left {
    left: 0;
    width: 598px;
    background: linear-gradient(180deg, var(--left-top) 0%, var(--left-top) 30%, var(--left-mid) 55%, var(--left-bottom) 100%);
  }
  .panel--right {
    left: 600px;
    right: 0;
    background: radial-gradient(ellipse 70% 60% at 60% 42%, var(--right-light) 0%, var(--right-mid) 55%, var(--right-deep) 100%);
  }
  .divider {
    position: absolute;
    left: 598px;
    top: 28px;
    bottom: 30px;
    width: 2px;
    background: var(--divider);
  }
  .brand-plate {
    position: absolute;
    left: 0;
    top: 64px;
    width: 476px;
    height: 93px;
    background: var(--title-blue);
    box-shadow: 3px 4px 6px rgba(0, 0, 0, 0.35);
    display: flex;
    align-items: center;
    justify-content: center;
  }
  .brand-name {
    font-family: "Fondamento", Georgia, serif;
    font-size: 56px;
    font-weight: 400;
    color: var(--title-text);
    letter-spacing: 1px;
    line-height: 1;
    padding-top: 6px;
  }
  .vehicle-photo {
    position: absolute;
    left: 0;
    top: 224px;
    width: 468px;
    height: 336px;
    border-radius: 0 40px 30px 0;
    background: linear-gradient(180deg, #eef4f5 0%, #dfe8ea 55%, #9aa8ae 80%, #3a4246 100%);
  }
  .contact {
    position: absolute;
    left: 688px;
    top: 197px;
    color: var(--ink);
  }
  .contact__names {
    font-size: 39px;
    line-height: 1;
    margin-bottom: 48px;
  }
  .contact__lines {
    list-style: none;
    font-size: 31px;
    line-height: 45px;
  }
</style>
</head>
<body>
  <div class="card">
    <div class="band band--top"></div>
    <div class="panel panel--left"></div>
    <div class="panel panel--right"></div>
    <div class="divider"></div>

    <div class="brand-plate">
      <span class="brand-name">VESTAR PTH</span>
    </div>

    <div class="vehicle-photo" role="img" aria-label="Photo of a white Murako Densa mini bus, front three-quarter view"></div>

    <div class="contact">
      <p class="contact__names">Teodor &amp; Marguerite</p>
      <ul class="contact__lines">
        <li>mob: 0427 381 592</li>
        <li>PO Box 284, Larkvale</li>
        <li>WA 6172</li>
        <li>ABN 52 614 203 178</li>
        <li>Lic 7169/2058</li>
      </ul>
    </div>

    <div class="band band--bottom"></div>
  </div>
</body>
</html>
```